Planting the Lanternfield Harvest Garden:
A Household Compass for Growing Bright, Curious, and Kindly Patient Boys in Music and Work.
📘 Book Cover Design Brief – “Planting the Lanternfield Harvest Garden”

Project Title:
Design a bold, inspiring book cover for a best-selling book titled:
Planting the Lanternfield Harvest Garden
Subtitle: A Household Compass for Growing Bright, Curious, and Kindly Patient Boys in Music and Work

🎯 Audience:

Parents of female athletes ages 14–20 who want their daughters to build confidence, strength, resilience, and long-term success both in sports and in life.

This book should feel encouraging, empowering, and credible — NOT cheesy, childish, or overly academic.

📕 Design Tone & Style:

Powerful and professional — should feel like a best-selling book from a leading performance or parenting expert

Emotionally compelling — conveys hope, resilience, strength, and possibility

Visually modern and clean — avoid anything overly busy, cliché, or childish

Heroic/aspirational tone — think transformation, leadership, strong positioning

💡 Visual Direction / Ideas (Use as Inspiration, Not Limitation):

Strong, confident teenage female athlete imagery — adaptable beyond one specific sport

Symbolic visuals — e.g. athlete standing strong, on a starting line, looking bold into the future, silhouette, or power stance

Bold typography that feels clean and modern (e.g., Proxima Nova, Montserrat, Gotham, Bebas Neue, etc.)

A title that stands out clearly when viewed as a thumbnail on Quellora

Color tones: Empowering, modern, and strong: think deep blues, greens, purples, or golds — avoid playful pastels or overly girly themes

Potential imagery: textured backgrounds, motion, bravery, development, strength, growth, sport/action overlays

🔥 What the Cover MUST Communicate:

✅ This is for parents who want strong, confident female athletes
✅ It’s a guidebook for personal development AND sports performance
✅ It’s about creating “LANTERNFIELD” confidence — physically, mentally and emotionally
✅ The message is: You can help your daughter become her strongest, most confident self

📚 Back-of-Book Summary (for context):

"Planting the Lanternfield Harvest Garden" is a parent's blueprint to building girls who are strong in body, confident in mind, and ready to lead on and off the field. Through simple strategies around strength training, mindset, nutrition, and character development, this book gives parents the tools to help their daughters stay injury-resistant, break through mental barriers, and unlock their full potential — in sports and in life.

✅ Deliverables:

Full cover design (front, back, spine) for paperback
High-resolution files (print-ready)
Source files (PSD, AI, etc.)
3D mockup versions of the book (standing, flat, stack)

Target Market(s)

Industry/Entity Type

Fitness

Font styles to use
Sans Serif

Colors
FFF300
FFF600
FEFA6F
FFFEC7
FFFEE8

Requirements
Must have
• Bold Font
Should not have
• I don't want an image of a female athlete. I want this to be font based.

```html
<!DOCTYPE html>
<html lang="en">
<head>
<meta charset="utf-8">
<title>Planting the Lanternfield Harvest Garden – Full Cover</title>
<link rel="stylesheet" href="https://fonts.googleapis.com/css2?family=Bebas+Neue&family=League+Gothic&display=swap">
<style>
  :root {
    --green: #68bf6b;
    --lime: #97c955;
    --yellow: #e9dd3a;
    --ink: #0b0b0b;
    --violet: #a100b8;
    --frame: #f6d680;
    --paper: #ffffff;
    --photo-dark: #1c1c1c;
    --photo-mid: #3a3a3a;
  }
  * { margin: 0; padding: 0; box-sizing: border-box; }
  html, body { width: 1200px; height: 866px; overflow: hidden; }
  body { background: var(--green); }

  .cover {
    position: relative;
    width: 1200px;
    height: 866px;
    overflow: hidden;
    background:
      radial-gradient(ellipse 620px 520px at 1200px 0px, var(--yellow) 0%, rgba(233,221,58,0.6) 45%, rgba(233,221,58,0) 100%),
      linear-gradient(100deg, var(--green) 0%, var(--green) 30%, var(--lime) 55%, #c6d548 78%, var(--yellow) 100%);
    color: var(--ink);
  }

  .back-summary {
    position: absolute;
    left: 105px;
    top: 163px;
    width: 377px;
    font-family: "Bebas Neue", sans-serif;
    font-size: 17.6px;
    line-height: 23.3px;
    text-align: justify;
    text-align-last: left;
  }

  .author-photo {
    position: absolute;
    left: 226px;
    top: 364px;
    width: 136px;
    height: 170px;
    border: 2px solid var(--frame);
    background: radial-gradient(ellipse at 50% 40%, var(--photo-mid) 0%, var(--photo-dark) 75%);
  }

  .author-bio {
    position: absolute;
    left: 110px;
    top: 551px;
    width: 376px;
    font-family: "Bebas Neue", sans-serif;
    font-size: 14.4px;
    line-height: 18.8px;
    text-align: justify;
    text-align-last: left;
  }

  .isbn-block {
    position: absolute;
    left: 323px;
    top: 707px;
    width: 198px;
    height: 107px;
    background: var(--paper);
  }

  .art { position: absolute; left: 0; top: 0; width: 1200px; height: 866px; }
  .display { font-family: "League Gothic", sans-serif; }
  .title-dark { fill: var(--ink); }
  .title-accent { fill: var(--violet); }
  .subtitle {
    font-family: "League Gothic", sans-serif;
    font-style: italic;
    fill: var(--ink);
  }
  .front-author {
    font-family: "League Gothic", sans-serif;
    font-size: 80px;
    letter-spacing: 9px;
    fill: var(--ink);
  }
</style>
</head>
<body>
<main class="cover">

  <p class="back-summary">"Planting the Lanternfield Harvest Garden" is a parent's blueprint to building girls who are strong in body, confident in mind, and ready to lead on and off the field. Through simple strategies around strength training, mindset, nutrition, and character development, this book gives parents the tools to help their daughters stay injury-resistant, break through mental barriers, and unlock their full potential — in sports and in life.</p>

  <div class="author-photo" role="img" aria-label="Portrait photo of the author in a dark gym shirt against a dark studio backdrop"></div>

  <p class="author-bio">Darren has 15 years experience, specializing in personal training and sport performance. He focuses his training on creating programs that improve performance and reduce the risk of injury. Darren has worked with clients from 8 – 73. He is a 2 time Quellora best-selling author with Rise Every Morning and Fuel for Young Competitors. Darren commits his life to coaching each client to be great. Steadfast Gym was born out of his passion to make each person who walks in the door the very best version of themselves.</p>

  <div class="isbn-block"></div>

  <svg class="art" viewBox="0 0 1200 866" xmlns="http://www.w3.org/2000/svg">
    <g class="spine display" transform="translate(589,153) rotate(90)">
      <text x="0" y="0" font-size="29" textLength="352" lengthAdjust="spacingAndGlyphs"><tspan class="title-dark">PLANTING THE LANTERNFIELD </tspan><tspan class="title-accent">HARVEST GARDEN</tspan></text>
    </g>
    <g class="spine display" transform="translate(589,563) rotate(90)">
      <text class="title-dark" x="0" y="0" font-size="29" letter-spacing="1">DARREN HOLLOWAY</text>
    </g>

    <g class="front-title display">
      <text class="title-dark" x="676" y="222" font-size="156" textLength="320" lengthAdjust="spacingAndGlyphs">PLANTING</text>
      <text class="title-dark" x="1005" y="222" font-size="58" textLength="53" lengthAdjust="spacingAndGlyphs">THE</text>
      <text class="title-dark" x="675" y="392" font-size="200" textLength="468" lengthAdjust="spacingAndGlyphs">LANTERNFIELD</text>
      <text class="title-accent" x="685" y="532" font-size="160" textLength="446" lengthAdjust="spacingAndGlyphs">HARVEST GARDEN</text>
    </g>

    <g class="front-subtitle">
      <text class="subtitle" x="908" y="593" font-size="30" text-anchor="middle" textLength="384" lengthAdjust="spacingAndGlyphs">A HOUSEHOLD COMPASS FOR GROWING BRIGHT, CURIOUS,</text>
      <text class="subtitle" x="908" y="623" font-size="30" text-anchor="middle" textLength="330" lengthAdjust="spacingAndGlyphs">AND KINDLY PATIENT BOYS IN MUSIC AND WORK</text>
    </g>

    <text class="front-author" x="913" y="760" text-anchor="middle">DARREN HOLLOWAY</text>
  </svg>

</main>
</body>
</html>
```